Anzeigengestaltung für Vertrieb von Kunststoffgittern
Zielgruppe
Vertrieb von Kunststoffgittern aus eigener Herstellung zur Bodenbefestigung. Einsatz in der Pferdehaltung. Böden von Paddocks und Ausläufen, Reitplätze, Reithallen, Führanlagen, Roundpen. Parkplatzbefestigung, Weidewege Freß- und Tränkplätze, Offenställe.
Wir benötigen eine neue Anzeige in diversen Pferdezeitschriften. Sie sollte ansprechend, mit hohem Wiedererkennunswert sein
Aufgabenstellung
Anzeige sollte für die Größe: 1/4 Seite mit Satzspiegel 43 x 270 mm, längs und 184 x 67 mm quer passen.
Die Anzeige sollte klar und ansprechend strukturiert sein, sie soll der Imagepflege dienen.
Die Farben Grün / Gelb wie im logo sollten vorherrschen. Ein innovativer Text ist gewünscht.
Zur Information kann die website: www.talbrek-gz.com dienen.
Weitere Fotos können zur Verfügung gestellt werden.

```html
<!DOCTYPE html>
<html lang="de">
<head>
<meta charset="utf-8">
<title>talbrek GZ – Anzeigen</title>
<link rel="stylesheet" href="https://fonts.googleapis.com/css2?family=Fira+Sans:wght@400;500&display=swap">
<style>
  :root {
    --green: #1f4c36;
    --orange: #e29b3b;
    --white: #ffffff;
    --sky: #9cc3e3;
    --field: #5b6a3c;
    --grid: #2b2f2a;
  }
  * { margin: 0; padding: 0; box-sizing: border-box; }
  html, body { width: 1171px; height: 1200px; overflow: hidden; background: var(--white); }
  body { position: relative; font-family: "Fira Sans", Arial, sans-serif; color: var(--white); }

  .brand {
    position: absolute; display: flex; align-items: center; gap: 8px;
    font-weight: 400; white-space: nowrap; line-height: 1;
  }
  .brand .mark { width: 10px; height: 10px; background: currentColor; flex: none; }

  /* Skyscraper ad */
  .ad-tall { position: absolute; left: 79px; top: 51px; width: 175px; height: 1097px; background: var(--green); overflow: hidden; }
  .ad-tall .top-band { position: absolute; left: 0; top: 0; width: 100%; height: 78px; background: var(--white); }
  .ad-tall .brand { left: 14px; top: 24px; font-size: 28px; color: var(--green); }
  .ad-tall .headline { position: absolute; left: 16px; top: 92px; font-weight: 500; text-transform: uppercase; line-height: 1.2; }
  .ad-tall .headline span { display: block; }
  .ad-tall .headline .h-small { font-size: 19px; }
  .ad-tall .headline .h-large { font-size: 26px; }
  .ad-tall .side-photo { position: absolute; left: 112px; top: 160px; width: 63px; height: 580px;
    background: linear-gradient(180deg, var(--sky) 0%, #c9dbe6 38%, #8a9566 55%, var(--field) 78%, #3a4430 100%); }
  .ad-tall .grid-photo { position: absolute; left: 0; top: 734px; width: 175px; height: 210px;
    background: linear-gradient(180deg, #3b4a33 0%, var(--grid) 55%, #4d5645 100%); }
  .ad-tall .copy { position: absolute; left: 14px; top: 168px; width: 100px; font-size: 12.5px; line-height: 24.5px; white-space: nowrap; }
  .ad-tall .copy p + p { margin-top: 24.5px; }
  .ad-tall .cta { position: absolute; left: 0; top: 948px; width: 165px; height: 140px; background: var(--orange); padding: 16px 10px 0 10px; }
  .ad-tall .cta h3 { font-weight: 400; font-size: 16.5px; margin-bottom: 20px; }
  .ad-tall .cta p { font-size: 13px; line-height: 22px; white-space: nowrap; display: flex; align-items: center; gap: 3px; }

  /* Banner ad */
  .ad-wide { position: absolute; left: 333px; top: 237px; width: 750px; height: 271px; background: var(--green); overflow: hidden; }
  .ad-wide .photo { position: absolute; left: 0; top: 0; width: 147px; height: 100%;
    background: linear-gradient(180deg, var(--sky) 0%, #bcd2e0 28%, #6f7a4e 40%, var(--field) 60%, var(--grid) 100%); }
  .ad-wide .frame { position: absolute; left: 6px; top: 8px; right: 6px; bottom: -4px; border: 2px solid var(--white); border-bottom: none; }
  .ad-wide .brand { left: 30px; top: 42px; font-size: 30px; color: var(--white); }
  .ad-wide .headline { position: absolute; left: 244px; top: 22px; font-size: 30px; font-weight: 400; text-transform: uppercase; letter-spacing: 0.3px; white-space: nowrap; }
  .ad-wide .lead { position: absolute; left: 310px; top: 69px; font-size: 14.5px; line-height: 23px; white-space: nowrap; }
  .ad-wide .detail { position: absolute; left: 310px; top: 128px; font-size: 11px; line-height: 22px; white-space: nowrap; }
  .ad-wide .cta { position: absolute; left: 310px; top: 190px; width: 416px; height: 81px; background: var(--orange); padding: 6px 8px; }
  .ad-wide .cta h3 { font-weight: 400; font-size: 19px; }
  .ad-wide .cta p { position: absolute; left: 106px; font-size: 13px; display: flex; align-items: center; gap: 10px; white-space: nowrap; }
  .ad-wide .cta .phone { top: 33px; }
  .ad-wide .cta .mail { top: 56px; }
  .icon { width: 15px; height: 15px; fill: var(--white); flex: none; }
</style>
</head>
<body>

<section class="ad-tall">
  <div class="top-band"></div>
  <div class="brand"><span class="mark"></span>talbrek GZ</div>
  <h2 class="headline"><span class="h-small">Befestigungen</span><span class="h-large">mit System</span></h2>
  <div class="side-photo" role="img" aria-label="Foto: Feld mit jungem Gras unter blauem Himmel"></div>
  <div class="grid-photo" role="img" aria-label="Foto: Kunststoff-Bodengitterplatten auf dem Feld"></div>
  <div class="copy">
    <p>Mit uns ist Ihr<br>Boden ideal<br>befestigt&nbsp; -<br>für alle<br>Einsatzbereiche!</p>
    <p>Schlamm und<br>Matsch<br>gehören der<br>Vergangenheit<br>an.</p>
    <p>Wir haben die<br>maßgeschneiderte<br>Lösung für<br>Bodenbefestigung<br>im Pferdesport<br>mit Paddock-<br>platten, für<br>befestigte<br>Flugplätze und<br>auch im Galabau<br>&amp; Tiefbau.</p>
  </div>
  <div class="cta">
    <h3>Jetzt informieren:</h3>
    <p><svg class="icon" viewBox="0 0 24 24"><path d="M6.6 10.8a15.1 15.1 0 0 0 6.6 6.6l2.2-2.2c.3-.3.7-.4 1-.2 1.1.4 2.3.6 3.6.6.6 0 1 .4 1 1V20c0 .6-.4 1-1 1A17 17 0 0 1 3 4c0-.6.4-1 1-1h3.5c.6 0 1 .4 1 1 0 1.3.2 2.5.6 3.6.1.3 0 .7-.2 1z"/></svg>034 21 - 58 07 19</p>
    <p>info@talbrek-gz.com</p>
    <p>www.talbrek-gz.com</p>
  </div>
</section>

<section class="ad-wide">
  <div class="photo" role="img" aria-label="Foto: Feld mit Bodengitterplatten unter blauem Himmel"></div>
  <div class="frame"></div>
  <div class="brand"><span class="mark"></span>talbrek GZ</div>
  <h2 class="headline">Befestigungen mit System</h2>
  <p class="lead">Mit uns ist Ihr Boden ideal befestigt&nbsp; – für alle Einsatzbereiche!<br>Schlamm und Matsch gehören der Vergangenheit an.</p>
  <p class="detail">Wir haben die maßgeschneiderte Lösung für Bodenbefestigung im Pferdesport<br>mit Paddockplatten, für befestigte Flugplätze und auch im Galabau &amp; Tiefbau.</p>
  <div class="cta">
    <h3>Jetzt informieren:</h3>
    <p class="phone"><svg class="icon" viewBox="0 0 24 24"><path d="M6.6 10.8a15.1 15.1 0 0 0 6.6 6.6l2.2-2.2c.3-.3.7-.4 1-.2 1.1.4 2.3.6 3.6.6.6 0 1 .4 1 1V20c0 .6-.4 1-1 1A17 17 0 0 1 3 4c0-.6.4-1 1-1h3.5c.6 0 1 .4 1 1 0 1.3.2 2.5.6 3.6.1.3 0 .7-.2 1z"/></svg>+49 (0)34 21 - 58 07 19</p>
    <p class="mail"><svg class="icon" viewBox="0 0 24 24"><path d="M2 5h20v14H2z M2 5l10 8 10-8" fill="none" stroke="#fff" stroke-width="2"/></svg>info@talbrek-gz.com&nbsp; |&nbsp; www.talbrek-gz.com</p>
  </div>
</section>

</body>
</html>
```